Werbeplakat für neues Webradio
Die Designerin konnte sich optimal in meine Wünsche und Vorstellungen hinein denken. ich bin mit dem Endresultat mehr als zufrieden.
Zielgruppe
Wir starten gerade ein kleines Webradio für eine sehr ländliche Region mit vielen Hügeln und viel Landwirtschaft. Daher auch der Name: Wiesenfunker.de Das Talwelle - Radio.
Wir sind nicht zu jung, aber auch nicht zu alt. Wir sind "Landeier" und stolz darauf.
Wir liefern neue Musik und Neues von hier. Wir sind nah am Leben und nah an den Menschen. Wir sind eigen - wir sind wir.Wir sind mittendrin - wir sind echte Wiesenfunker :-)
Aufgabenstellung
Liebe Designer.
Begleitend zum Sendestart unseres Webradios wollen wir mit einer Flyer- und Plakat-Kampagne auf uns aufmerksam machen.
Es soll ein absoluter Eyecatcher werden und für den nötigen "Talk of Dorf" sorgen.
Nicht zu spießig, aber auch nicht zu jung.
Jeder soll nach dem Betrachten Lust haben einfach mal reinzuhören!!!
Verwendet werden sollen unser Logo und der beinhaltete Name
"Wiesenfunker.de - Das Talwelle Radio".
Wo und wie Ihr alles platziert, wisst ihr besser als ich!
Zudem bitte folgende Textelemente: (Anordnung wie ihr es am besten findet)
-Neue Musik und Neues von hier
-Jetzt einschalten - Im Web oder per App - www.wiesenfunker.de
Irgendwo auf dem Plakat sollte noch etwas Platz bleiben, auf dem später hoffentlich die Logos von Sponsoren bzw. Werbekunden auftauchen werden. :-)
Unser Logo habe ich beigefügt (in mehreren Dateiformen)
Ich bin sehr gespannt auf Eure Umsetzungen und danke jedem der mitmacht von Herzen für seinen/ihren Einsatz!
Wenn Fragen da sind - einfach her damit. Ich antworte zeitnah
Cheerio
Rüdiger

```html
<!DOCTYPE html>
<html lang="de">
<head>
<meta charset="utf-8">
<title>Wiesenfunker.de – Plakat</title>
<link rel="stylesheet" href="https://fonts.googleapis.com/css2?family=Barlow+Condensed:wght@500;600&family=Open+Sans:wght@400;700&display=swap">
<style>
  :root {
    --green: #84b800;
    --orange: #e36300;
    --paper: #ffffff;
    --grey: #9a9a9a;
    --grey-dark: #8a8a8a;
  }
  * { margin: 0; padding: 0; box-sizing: border-box; }
  html, body { width: 849px; height: 1200px; overflow: hidden; background: var(--paper); }
  .poster { position: relative; width: 849px; height: 1200px; overflow: hidden; background: var(--paper); font-family: "Barlow Condensed", sans-serif; }
  .photo { position: absolute; inset: 0; }
  .headline { position: absolute; left: 76px; top: 210px; font-weight: 600; font-size: 136px; line-height: 120px; letter-spacing: -4px; }
  .headline span { display: block; }
  .headline .green { color: var(--green); }
  .headline .orange { color: var(--orange); }
  .call { position: absolute; left: 83px; top: 568px; color: var(--green); font-weight: 500; font-size: 48px; line-height: 54px; }
  .station { position: absolute; left: 259px; top: 965px; display: flex; align-items: center; gap: 22px; }
  .station-mark { width: 150px; height: 150px; border-radius: 50%; background: var(--orange); flex: none; }
  .station-name { color: var(--green); font-weight: 600; font-size: 50px; line-height: 46px; letter-spacing: -0.5px; }
  .sponsors { position: absolute; left: 285px; top: 1155px; display: flex; gap: 26px; align-items: center; font-family: "Open Sans", sans-serif; font-size: 16px; color: var(--grey); }
  .sponsor { display: flex; align-items: center; gap: 9px; }
  .sponsor .square { width: 22px; height: 22px; background: var(--grey-dark); }
  .sponsor .circle { width: 27px; height: 27px; border-radius: 50%; background: var(--grey-dark); }
  .sponsor.bold { font-weight: 700; }
</style>
</head>
<body>
<div class="poster">
  <svg class="photo" width="849" height="1200" viewBox="0 0 849 1200" role="img" aria-label="Foto: Mann in gelber Jacke und Jeans auf einer Wiese, dahinter ein alter roter Traktor im hohen Gras">
    <defs>
      <linearGradient id="sceneTone" x1="0" y1="0" x2="0" y2="1">
        <stop offset="0" stop-color="#e6dcb8"/>
        <stop offset="0.35" stop-color="#e9bd5e"/>
        <stop offset="0.65" stop-color="#a9c2cf"/>
        <stop offset="0.85" stop-color="#d9957f"/>
        <stop offset="1" stop-color="#b7d27a"/>
      </linearGradient>
      <radialGradient id="skyFade" cx="220" cy="360" r="600" gradientUnits="userSpaceOnUse">
        <stop offset="0" stop-color="#fff" stop-opacity="1"/>
        <stop offset="0.6" stop-color="#fff" stop-opacity="0.95"/>
        <stop offset="1" stop-color="#fff" stop-opacity="0"/>
      </radialGradient>
    </defs>
    <path d="M0,0 H849 V903 Q380,880 0,1015 Z" fill="url(#sceneTone)"/>
    <path d="M0,0 H849 V903 Q380,880 0,1015 Z" fill="url(#skyFade)"/>
  </svg>

  <h1 class="headline">
    <span class="green">Neue Musik</span>
    <span class="orange">und Neues</span>
    <span class="orange">von hier</span>
  </h1>

  <p class="call">Jetzt einschalten –<br>Im Web oder per App<br>www.wiesenfunker.de</p>

  <div class="station">
    <div class="station-mark"></div>
    <div class="station-name">Wiesenfunker.de<br>Das Talwelle-Radio</div>
  </div>

  <div class="sponsors">
    <div class="sponsor bold"><span class="square"></span>Muster Logo</div>
    <div class="sponsor"><span class="circle"></span>Muster Logo</div>
    <div class="sponsor"><span class="square"></span>Muster Logo</div>
  </div>
</div>
</body>
</html>
```